Moonvale Jewellery Limited - designer pearl and silver jewellery

Designer silver jewellery with a twist that 20% of the net profit will be donated to a charity in India to help abused children

The products are designed to make the wearer not only feel good about how good the jewellery looks but to know they are also helping others less fortunate

All the Jewellery is designed by myself Margaret Doyle and made in 925 Hallmarked sterling silver . The hallmarking is carried out by the Corrick Assay office

This is my first website and will need to be suitable for e-commerce

Target Market(s)

Stylish women with a love of simple and elegant design , not high fashion by timeless simplicity

Number of Pages Required

5+ page

Font styles to use
Sans Serif

Colors
e666a6

Requirements
Must have
• Reference to Sterling silver
• The Pantone ref for my logo background now is white out of 2063
Nice to have
• Fresh and contemporary - Aimed at 25-55 market
• The same consumer would
• Like this product as likes Velmira, Kester Dunne but will also appreciate the fact this product is about helping others as well
• The Jewellery is about clean simple lines , elegance , hand made and styled to be timeless
• The products are designed to be casual and elegant and all feature either natural freshwater pearls or semi precious gemstones
• I also would like a page that customers can arrange to book talks about the design and production of the product . I give these talks generally tomladies groups and explain the manufacturing process and what the charity I’m doing supports

```html
<!DOCTYPE html>
<html lang="en">
<head>
<meta charset="utf-8">
<title>Moonvale Jewellery</title>
<link rel="stylesheet" href="https://fonts.googleapis.com/css2?family=Tenor+Sans&display=swap">
<style>
  :root {
    --ink: #1e1e1e;
    --black: #000000;
    --white: #ffffff;
    --gold: #e2cd7a;
    --gold-deep: #b99a3e;
    --rule: #e9c12b;
    --cream: #f4e7c2;
    --field-border: #b5b5b5;
  }
  * { box-sizing: border-box; margin: 0; padding: 0; }
  html, body { width: 1200px; height: 640px; overflow: hidden; background: var(--white); }
  body { position: relative; font-family: "Tenor Sans", sans-serif; color: var(--ink); }
  a { color: inherit; text-decoration: none; }

  .site-header { position: absolute; left: 0; top: 0; width: 1200px; height: 117px; background: var(--black); }
  .utility-link { position: absolute; top: 53px; color: var(--white); font-size: 13.5px; letter-spacing: 0.2px; }
  .brand { position: absolute; left: 0; width: 1200px; top: 26px; text-align: center; color: var(--gold); }
  .brand-name { display: block; font-size: 40px; line-height: 44px; letter-spacing: 1px; }
  .brand-sub { display: block; font-size: 16px; line-height: 20px; letter-spacing: 2px; }

  .category-nav { position: absolute; left: 0; top: 117px; width: 1200px; height: 37px; background: var(--white); }
  .category-link { position: absolute; top: 11px; font-size: 12.8px; letter-spacing: 0.2px; }

  .footer-band { position: absolute; left: 0; top: 154px; width: 1200px; height: 84px;
    background: linear-gradient(to bottom, var(--cream), var(--white)); }

  .footer-heading { position: absolute; top: 200px; font-size: 14.5px; letter-spacing: 0.3px; }
  .footer-rule { position: absolute; left: 347px; top: 221px; width: 546px; height: 4px; background: var(--rule); }

  .link-list { position: absolute; top: 267px; list-style: none; }
  .link-list li { height: 32px; font-size: 12.5px; line-height: 20px; }

  .social-list { position: absolute; left: 828px; top: 262px; list-style: none; }
  .social-list li { height: 38px; display: flex; align-items: center; gap: 5px; font-size: 10px; color: var(--gold-deep); }
  .social-dot { width: 13px; height: 13px; border-radius: 50%; background: var(--gold-deep); flex: none; }

  .signup { position: absolute; left: 473px; top: 523px; display: flex; align-items: center; }
  .signup-label { font-size: 9.5px; width: 94px; }
  .signup-field { width: 246px; height: 27px; border: 1px solid var(--field-border); background: var(--white); }
  .signup-send { margin-left: 9px; width: 50px; height: 30px; display: block; }
</style>
</head>
<body>
  <header class="site-header">
    <a class="utility-link" style="left:58px" href="#">HOME</a>
    <a class="utility-link" style="left:133px" href="#">SEARCH</a>
    <div class="brand">
      <span class="brand-name">moonvale</span>
      <span class="brand-sub">JEWELLERY</span>
    </div>
    <a class="utility-link" style="left:997px" href="#">FIND STORE</a>
    <a class="utility-link" style="left:1101px" href="#">SIGN IN</a>
  </header>

  <nav class="category-nav">
    <a class="category-link" style="left:344px" href="#">BRACELETS</a>
    <a class="category-link" style="left:447px" href="#">RINGS</a>
    <a class="category-link" style="left:525px" href="#">EARINGS</a>
    <a class="category-link" style="left:607px" href="#">NECKLACES</a>
    <a class="category-link" style="left:708px" href="#">GIFTS</a>
    <a class="category-link" style="left:777px" href="#">SUPPORT THE KIDS</a>
  </nav>

  <footer>
    <div class="footer-band"></div>
    <h2 class="footer-heading" style="left:347px">HELP</h2>
    <h2 class="footer-heading" style="left:490px">MANAGE</h2>
    <h2 class="footer-heading" style="left:643px">ABOUT US</h2>
    <h2 class="footer-heading" style="left:797px">CONTACT US</h2>
    <div class="footer-rule"></div>

    <ul class="link-list" style="left:347px">
      <li>FAQs</li><li>Oders</li><li>Shipping</li><li>Returns</li>
      <li>Size Gude</li><li>Product &amp; Care</li><li>Warranty</li>
    </ul>
    <ul class="link-list" style="left:488px">
      <li>Gift Cards</li><li>My Account</li><li>My Orders</li>
      <li>My Wish List</li><li>Order Status</li><li>Preferred Card</li>
    </ul>
    <ul class="link-list" style="left:642px">
      <li>Explore the Brand</li><li>Careers</li><li>Store Locator</li>
      <li>Promotions and Offers</li><li>Terms and Conditions</li>
    </ul>
    <ul class="social-list">
      <li><span class="social-dot"></span>Chatterly</li>
      <li><span class="social-dot"></span>Flitter</li>
      <li><span class="social-dot"></span>Reelhub</li>
      <li><span class="social-dot"></span>Snapfold</li>
      <li><span class="social-dot"></span>Pinlane</li>
    </ul>

    <form class="signup">
      <label class="signup-label" for="email">Enter Email Address</label>
      <input class="signup-field" id="email" type="email">
      <svg class="signup-send" viewBox="0 0 50 30" aria-label="Send">
        <rect x="0" y="0" width="50" height="30" fill="var(--gold-deep)"/>
        <path d="M0 0 L25 17 L50 0 M0 30 L19 13 M50 30 L31 13" fill="none" stroke="var(--white)" stroke-width="1.2"/>
      </svg>
    </form>
  </footer>
</body>
</html>
```